New Property management company business cards

Looking for a new business card, to reflect new younger ownership
Card should be clean, simple and professional but with a modern layout that is conveys our new logo and business model

Key aspects of the business:

Property Management
Facility Maintenance
Project Management
Tenant Improvements

Mailing Address:
PO BOX 7816
Lakeford CA, 95420

Phone: 209-418-6071
Direct: 209-418-6074

Doyle Marsh
President

Target Market(s)

Commercial property owners

Industry/Entity Type

Real Estate property management

Contact Information for Business Card

Open to all designs but lean toward vertical layouts

Requirements
Must have
• Logo and space to customize name and contact info

```html
<!DOCTYPE html>
<html lang="en">
<head>
<meta charset="utf-8">
<title>Meridale Property Management – Business Card</title>
<link href="https://fonts.googleapis.com/css2?family=Montserrat:wght@400;500;700&display=swap" rel="stylesheet">
<style>
  :root{
    --bg:#8a8a87;
    --card-white:#ffffff;
    --navy:#32323f;
    --teal:#1fa9a0;
    --ink:#3a3a48;
    --muted:#5a5a66;
    --back-text:#6b6b85;
  }
  *{box-sizing:border-box;margin:0;padding:0}
  html,body{width:1200px;height:801px;overflow:hidden}
  body{background:var(--bg);font-family:"Montserrat",Arial,sans-serif;position:relative}
  .card{position:absolute;top:252px;width:520px;height:297px;border-radius:2px;box-shadow:0 10px 24px rgba(0,0,0,.25)}
  .card--front{left:50px;background:var(--card-white);border-bottom:4px solid var(--teal)}
  .card--back{left:630px;background:var(--navy);border-bottom:3px solid var(--teal)}
  .brand{position:absolute;left:28px;top:0;width:222px;height:100%;display:flex;align-items:center;gap:10px}
  .brand__mark{width:18px;height:18px;background:var(--teal);flex:none}
  .brand__name{font-weight:700;font-size:17px;letter-spacing:.08em;color:var(--ink);line-height:1.25;text-transform:uppercase}
  .divider{position:absolute;left:262px;top:40px;width:2px;height:215px;background:var(--teal)}
  .contact{position:absolute;left:284px;top:44px;color:var(--muted);font-size:13px;line-height:1.5}
  .contact__name{color:var(--teal);font-weight:700;font-size:21px;letter-spacing:.02em;line-height:1.1}
  .contact__title{margin-bottom:14px}
  .contact__address{margin-bottom:14px}
  .contact__row{display:flex;align-items:center;gap:7px}
  .contact__row svg{width:11px;height:11px;flex:none}
  .back-name{position:absolute;inset:0;display:flex;align-items:center;justify-content:center;font-weight:700;font-size:22px;letter-spacing:.12em;color:var(--back-text);text-transform:uppercase}
</style>
</head>
<body>
  <section class="card card--front">
    <div class="brand">
      <span class="brand__mark"></span>
      <span class="brand__name">Meridale<br>Property Management</span>
    </div>
    <div class="divider"></div>
    <div class="contact">
      <div class="contact__name">DOYLE MARSH</div>
      <div class="contact__title">President</div>
      <div class="contact__address">PO BOX 7816<br>Lakeford CA, 95420</div>
      <div class="contact__row">
        <svg viewBox="0 0 12 12"><path d="M2 1h3l1 3-2 1a7 7 0 0 0 3 3l1-2 3 1v3c-6 1-10-3-9-9z" fill="#1fa9a0"/></svg>209-418-6071</div>
      <div class="contact__row">
        <svg viewBox="0 0 12 12"><rect x="3" y="1" width="6" height="10" rx="1" fill="none" stroke="#1fa9a0" stroke-width="1.4"/></svg>209-418-6074</div>
      <div class="contact__row">
        <svg viewBox="0 0 12 12"><rect x="1" y="2.5" width="10" height="7" fill="#1fa9a0"/><path d="M1 2.5l5 4 5-4" fill="none" stroke="#fff" stroke-width="1"/></svg>info@meridaleproperty.com</div>
      <div class="contact__row">
        <svg viewBox="0 0 12 12"><circle cx="6" cy="6" r="5" fill="#1fa9a0"/><path d="M1 6h10M6 1c-2 3-2 7 0 10M6 1c2 3 2 7 0 10" fill="none" stroke="#fff" stroke-width=".8"/></svg>www.meridaleproperty.com</div>
    </div>
  </section>
  <section class="card card--back">
    <div class="back-name">Meridale</div>
  </section>
</body>
</html>
```